Bow Tie Post Card (Post Card to Package a Children's Bow Tie)

Bowties have been added to our company's inventory and we want to print postcards to package and fasten them to (please see images for an example).

Please use the attached photos for reference. I would like to use the head portion of our logo and remove the tie to leave a spot for an actual tie. I want something fun and clever to look at. Something that is thoughtful cute when people open it. Maybe a fun patterned background or a boarder? It could say The Kite Crate or www.thekitecrate.com on there somewhere if there is space or seems right but does not have to.

The post cards are 4x6 inches. The bow ties themselves are about 3.5x2 inches.

Thank you.

Target Market(s)

Children's clothing and accessories.

Industry/Entity Type

It Company

Font styles to use
Sans Serif

Requirements
Must have
• Must use the same coloring of the brand. Please see the website for reference. These are the color colors used:
• 86CFC6
• 568686
• F3F2F0
• 757575
• CF1313
• *other colors may be used but these are the general brand colors.
• Font: Century Gothic Regular and Black Larch
Nice to have
• Should be nice, clean, modern and fun.

```html
<!DOCTYPE html>
<html lang="en">
<head>
<meta charset="utf-8">
<title>The Kite Crate – Bow Tie Postcard</title>
<link rel="stylesheet" href="https://fonts.googleapis.com/css2?family=Oswald:wght@500;600&family=Questrial&family=Open+Sans:wght@400;700&family=Lobster&display=swap">
<style>
  :root{
    --teal:#86cfc6;
    --teal-dark:#568686;
    --paper:#f3f2f0;
    --grey:#757575;
    --red:#cf1313;
    --ink:#1d1d1d;
    --white:#ffffff;
    --bg:#e9e9e9;
  }
  *{box-sizing:border-box;margin:0;padding:0}
  html,body{width:1200px;height:1200px;overflow:hidden;background:var(--bg)}
  body{position:relative;font-family:"Open Sans",sans-serif;color:var(--ink)}

  .card{position:absolute;left:172px;width:845px;height:564px;background:var(--white);overflow:hidden}
  .card--front{top:24px}
  .card--back{top:612px}
  .card svg.shapes{position:absolute;inset:0;width:100%;height:100%}
  .abs{position:absolute}

  /* front */
  .brand-mark{left:70px;top:70px;width:230px;height:200px;display:flex;flex-direction:column;align-items:center;justify-content:center;gap:14px}
  .brand-mark__dot{width:120px;height:120px;border-radius:50%;border:16px solid var(--teal)}
  .brand-mark__name{font-family:"Questrial",sans-serif;font-size:30px;color:var(--teal)}
  .bowtie-slot{left:116px;top:300px;width:168px;height:130px;border-radius:10px;
    background:linear-gradient(135deg,#7a2a3a,#b06a3a 50%,#5a3b6a)}
  .headline{right:90px;top:70px;text-align:right}
  .headline__kicker{font-family:"Oswald",sans-serif;font-weight:600;font-size:37px;color:var(--red);letter-spacing:.5px;line-height:1.1}
  .headline__main{font-family:"Open Sans",sans-serif;font-size:43px;line-height:1.1}
  .intro{left:420px;top:176px;width:336px;font-size:12.6px;line-height:1.32;text-align:justify}
  .call{left:420px;top:334px;font-family:"Oswald",sans-serif;font-weight:600;font-size:27px;color:var(--red);white-space:nowrap}
  .call span{color:var(--ink)}
  .kid-photo{left:545px;top:386px;width:285px;height:158px;border-radius:30px 30px 8px 8px;
    background:linear-gradient(160deg,#b37b4e,#6fb9a4 60%,#c96a2c)}
  .url-pill{background:var(--white);border-radius:5px;font-family:"Questrial",sans-serif;font-size:19px;padding:3px 10px}
  .card--front .url-pill{left:56px;top:499px;width:220px}

  /* back */
  .works-bar{left:0;top:30px;width:282px;height:38px;background:var(--teal);
    font-family:"Lobster",cursive;font-size:29px;padding-left:34px;line-height:38px}
  .works-intro{left:32px;top:86px;width:244px;font-size:15.5px;line-height:1.3;text-align:justify}
  .step{left:32px;width:240px;border:1.5px solid var(--grey);border-radius:6px;padding:6px 8px;display:flex;gap:8px}
  .step__label{position:absolute;left:18px;top:4px;font-size:11px;font-weight:700}
  .step__icon{flex:0 0 52px;margin-top:16px;height:52px;border-radius:6px;background:var(--teal)}
  .step__icon--round{border-radius:50%}
  .step__text{font-size:9.6px;line-height:1.32;text-align:justify;color:#222}
  .side-photo{left:294px;top:0;width:213px;height:490px;border-right:4px solid var(--red);border-bottom:4px solid var(--red);
    border-radius:0 0 10px 0;background:linear-gradient(170deg,#c9b98a,#9fb07a 40%,#8fa0b8 70%,#3b5f8f)}
  .back-brand{left:535px;top:36px;display:flex;align-items:center;gap:8px;font-family:"Questrial",sans-serif;font-size:20px;color:var(--teal)}
  .back-brand i{width:12px;height:12px;border-radius:50%;background:var(--red)}
  .stamp{left:747px;top:26px;width:50px;height:90px;border:1px solid var(--grey)}
  .address-line{left:546px;width:236px;height:1.5px;background:#b5b5b5}
  .back-call{left:54px;top:529px;font-family:"Questrial",sans-serif;font-size:18px;color:var(--white);letter-spacing:.5px}
  .card--back .url-pill{left:545px;top:527px;width:245px;text-align:center}
</style>
</head>
<body>

<section class="card card--front">
  <svg class="shapes" viewBox="0 0 845 564" aria-hidden="true">
    <polygon points="0,445 845,508 845,564 0,564" fill="var(--teal)"/>
    <polygon points="518,502 845,376 845,508" fill="var(--red)"/>
  </svg>
  <div class="abs brand-mark">
    <div class="brand-mark__dot"></div>
    <div class="brand-mark__name">The Kite Crate</div>
  </div>
  <div class="abs bowtie-slot" role="img" aria-label="Woven multicolour children's bow tie"></div>
  <div class="abs headline">
    <div class="headline__kicker">CONVENIENT, STYLISH</div>
    <div class="headline__main">Attire Delivered</div>
  </div>
  <p class="abs intro"><b>The Kite Crate</b> is to provide your child with stylish clothing and accessories. Each box is carefully crafted to be trendy, seasonally appropriate and comfortable. We understand it is difficult to find fantastic clothing geared towards boys and aim to make it more affordable and easy. The Kite Crate currently offers single purchase boxes and gifts available in our <b>Crate Boutique</b>.</p>
  <div class="abs call">CALL NOW: <span>000-000-0000</span></div>
  <div class="abs kid-photo" role="img" aria-label="Young boy in sunglasses, brown jacket and mint trousers sitting on the floor"></div>
  <div class="abs url-pill">www.thekitecrate.com</div>
</section>

<section class="card card--back">
  <svg class="shapes" viewBox="0 0 845 564" aria-hidden="true">
    <rect x="0" y="504" width="845" height="60" fill="var(--teal)"/>
    <polygon points="672,512 845,475 845,512" fill="var(--red)"/>
  </svg>
  <h2 class="abs works-bar">How It Works</h2>
  <p class="abs works-intro"><b>The Kite Crate</b> delivers stylized clothing and accessories geared towards boys sized three months to 5T.</p>

  <div class="abs step" style="top:170px;height:96px">
    <span class="step__label">Step-1</span>
    <div class="step__icon step__icon--round" role="img" aria-label="Sizing icon"></div>
    <p class="step__text">Sign up. Select your child's sizing and our teams will get to work styling an ensemble for your little one. Once you've subscribed, check out our online Crate Boutique for add ons to your monthly order.</p>
  </div>
  <div class="abs step" style="top:284px;height:96px">
    <span class="step__label">Step-2</span>
    <div class="step__icon" role="img" aria-label="Delivery box icon"></div>
    <p class="step__text" style="margin-top:14px">Receive a Kite Crate every month! Check your email for tracking information and patiently await for your box to arrive at your doorstep.</p>
  </div>
  <div class="abs step" style="top:396px;height:98px">
    <span class="step__label">Step-3</span>
    <div class="step__icon" role="img" aria-label="Shirt and shorts icon"></div>
    <p class="step__text" style="margin-top:14px">Dress to Impress! Enjoy your new clothing and accessories. We love seeing your dashing dudes on social media in our items. Tag us @thekitecrate and #thekitecrate</p>
  </div>

  <div class="abs side-photo" role="img" aria-label="Smiling boy in a grey fedora and plaid shirt sitting outdoors"></div>

  <div class="abs back-brand"><i></i>The Kite Crate</div>
  <div class="abs stamp"></div>
  <div class="abs address-line" style="top:263px"></div>
  <div class="abs address-line" style="top:290px"></div>
  <div class="abs address-line" style="top:318px"></div>
  <div class="abs address-line" style="top:347px"></div>

  <div class="abs back-call">CALL: 000-000-0000</div>
  <div class="abs url-pill">www.thekitecrate.com</div>
</section>

</body>
</html>
```